LOS PINARES DE ORO - EXCLUSIVE AND LUXURY REAL ESTATE PROJECT

Se trata del diseño de un mono poste grande (4 m x 2 m) o (8m x 3m) anunciando la construcción de 30 villas de lujo en un terreno en primera línea de playa en el sur de España (Cádiz).

La idea es crear expectación y transmitir lujo y exclusividad.

Target Market(s)

Clientes de alto poder adquisitivo que quieran adquirir su segunda vivienda en un entorno privilegiado a escasos pasos de una de las playas más bonitas de Cádiz.

Industry/Entity Type

REAL ESTATE

Colors

Designer to choose colors to be used in the design.

Requirements
Must have
• LOS PINARES DE ORO as the name of the development
Nice to have
• Crear expectación con ideas del tipo: “Coming soon” o “No te lo puedes perder”

```html
<!DOCTYPE html>
<html lang="es">
<head>
<meta charset="utf-8">
<title>Los Pinares De Oro – Coming Soon</title>
<link rel="stylesheet" href="https://fonts.googleapis.com/css2?family=Playfair+Display:wght@400&family=Roboto+Slab:wght@400&display=swap">
<style>
  :root {
    --backdrop: #d9d9d9;
    --banner-black: #111111;
    --ivory: #f6f1e6;
    --gold-deep: #c99a1c;
    --gold-light: #f3e3a8;
    --gold-mid: #b8892a;
  }
  html, body {
    margin: 0;
    padding: 0;
    width: 1200px;
    height: 900px;
    overflow: hidden;
    background: var(--backdrop);
  }
  .canvas {
    position: relative;
    width: 1200px;
    height: 900px;
  }
  .banner {
    position: absolute;
    left: 40px;
    top: 170px;
    width: 1120px;
    height: 560px;
  }
  .banner-subline {
    font-family: "Roboto Slab", Georgia, serif;
    font-size: 40px;
    fill: var(--ivory);
    letter-spacing: 1px;
  }
  .banner-headline {
    font-family: "Playfair Display", "Times New Roman", serif;
    font-size: 118px;
    font-weight: 400;
  }
</style>
</head>
<body>
<main class="canvas">
  <svg class="banner" viewBox="0 0 1120 560" xmlns="http://www.w3.org/2000/svg" aria-label="Coming Soon – 30 Villas De Lujo – Los Pinares De Oro">
    <defs>
      <linearGradient id="gold-foil" x1="0" y1="0" x2="1" y2="0">
        <stop offset="0" stop-color="var(--gold-deep)"/>
        <stop offset="0.25" stop-color="var(--gold-light)"/>
        <stop offset="0.5" stop-color="var(--gold-mid)"/>
        <stop offset="0.75" stop-color="var(--gold-light)"/>
        <stop offset="1" stop-color="var(--gold-deep)"/>
      </linearGradient>
    </defs>

    <rect class="banner-field" width="1120" height="560" fill="var(--banner-black)"/>

    <g class="gold-frame" fill="none" stroke="url(#gold-foil)" stroke-width="4">
      <rect class="frame-outer" x="121" y="128" width="880" height="305"/>
      <polygon class="frame-band" points="107,201 1025,201 1053,281 1025,361 107,361 70,281"/>
    </g>

    <rect x="119" y="203" width="884" height="156" fill="none"/>

    <text class="banner-subline" x="560" y="181" text-anchor="middle">30 Villas De Lujo</text>
    <text class="banner-headline" x="560" y="315" text-anchor="middle" fill="url(#gold-foil)">Coming Soon</text>
    <text class="banner-subline" x="560" y="414" text-anchor="middle">Los Pinares De Oro</text>
  </svg>
</main>
</body>
</html>
```